Book cover for a very impressive real-life healing story from a stage IV deadly disease

I need a book cover design for the French translation of the US book http://www.pagevendo.com/Tims-Journey-Fever-Outlasted-Illness/dp/0845512097/ref=sr_1_4?s=books&ie=UTF8&qid=1455100794&sr=1-4&keywords=kit+marsh
.
I do not want the word AIDS on the French cover, as the story of this book applies to any disease.

The french title will be something like :
Un nouveau matin !
Condamné par la médecine, il guérit grâce au jeûne, la détoxination, et l’amour.

which means something like
A new morning!
Subtitle : Given up by official medecine, he managed to heal with fasting, detox and love.

Many thanks !

Target Market(s)

Anybody interested in natural health

Requirements
Must have
• Nothing special
Nice to have
• Nothing special
Should not have
• Nothing special

```html
<!DOCTYPE html>
<html lang="fr">
<head>
<meta charset="utf-8">
<title>Un nouveau matin ! — couverture</title>
<link href="https://fonts.googleapis.com/css2?family=Alfa+Slab+One&family=Source+Sans+3:wght@300;400&family=Montserrat:wght@400&display=swap" rel="stylesheet">
<style>
  :root {
    --stage: #e4e5e6;
    --paper: #ffffff;
    --title-blue: #7dbde6;
    --text-blue: #1f6fa3;
    --cell-green: #b9d97a;
    --cell-yellow: #e4e32a;
    --rule: #555555;
  }
  * { box-sizing: border-box; margin: 0; padding: 0; }
  html, body { width: 1200px; height: 850px; overflow: hidden; }
  body {
    background: var(--stage);
    position: relative;
    font-family: "Source Sans 3", sans-serif;
  }
  .wrap {
    position: absolute;
    left: 70px; top: 65px;
    width: 1060px; height: 720px;
    display: flex;
    box-shadow: 0 10px 30px rgba(0,0,0,0.12);
  }
  .panel { position: relative; background: var(--paper); overflow: hidden; }
  .back { width: 500px; }
  .spine { width: 60px; border-left: 1px solid #eee; border-right: 1px solid #eee; }
  .front { width: 500px; }

  .cells { position: absolute; display: block; }

  /* Front cover */
  .title {
    position: absolute; left: 40px; top: 40px; width: 420px;
    font-family: "Alfa Slab One", serif;
    color: var(--title-blue);
    line-height: 0.95;
  }
  .title .small { display: block; font-size: 52px; padding-left: 110px; }
  .title .big { display: block; font-size: 84px; }
  .title .indent { padding-left: 90px; }
  .subtitle {
    position: absolute; right: 40px; top: 320px; width: 300px;
    text-align: right;
    color: var(--title-blue);
    font-weight: 300; font-size: 17px; line-height: 1.3;
  }
  .author {
    position: absolute; left: 80px; bottom: 55px;
    color: var(--title-blue);
    font-weight: 400; font-size: 36px; line-height: 1.05;
    text-transform: uppercase;
  }

  /* Back cover */
  .blurb {
    position: absolute; left: 55px; top: 400px; width: 380px;
    font-family: "Montserrat", sans-serif;
    color: var(--text-blue);
    font-size: 15.5px; line-height: 1.45;
  }
  .isbn-box {
    position: absolute; right: 60px; bottom: 70px;
    width: 120px; height: 24px;
    border: 1px solid var(--rule);
  }

  /* Spine */
  .spine-title {
    position: absolute; left: 50%; top: 40px;
    transform: translateX(-50%) rotate(90deg) translateX(50%);
    transform-origin: center;
    white-space: nowrap;
    font-family: "Alfa Slab One", serif;
    color: var(--title-blue);
    font-size: 22px;
  }
  .spine-text {
    position: absolute; left: 50%; top: 60px;
    writing-mode: vertical-rl;
    transform: translateX(-50%);
    font-family: "Alfa Slab One", serif;
    color: var(--title-blue);
    font-size: 22px;
  }
  .spine-author {
    position: absolute; left: 50%; bottom: 40px;
    writing-mode: vertical-rl;
    transform: translateX(-50%);
    color: var(--title-blue);
    font-size: 14px; line-height: 1.1;
    text-transform: uppercase;
  }
</style>
</head>
<body>
<main class="wrap">
  <section class="panel back">
    <svg class="cells" width="500" height="380" viewBox="0 0 500 380" role="img" aria-label="Motif de cellules vertes translucides à noyaux jaunes">
      <defs>
        <linearGradient id="back-cells" x1="0" y1="0" x2="1" y2="1">
          <stop offset="0" stop-color="#c6e08f"/>
          <stop offset="0.6" stop-color="#b9d97a"/>
          <stop offset="1" stop-color="#d3e06a"/>
        </linearGradient>
      </defs>
      <path d="M0 0 H500 V380 C430 360 380 300 300 320 C220 340 150 300 90 270 C40 245 10 200 0 180 Z" fill="url(#back-cells)" opacity="0.85"/>
    </svg>
    <p class="blurb">Lorem ipsum dolor sit amet, consectetur adipiscing elit. Nam pharetra sodales est, quis justo consectetur vel. Donec sollicitudin magna, vitae ultrices mauris ullamcorper. Donec at interdum lacus. Donec sagittis nisi vel hendrerit. Etiam ac tincidunt mi. Nisi vel nibh convallis tempor. Nunc vitae maximus nec, sagittis sed massa.</p>
    <div class="isbn-box"></div>
  </section>

  <section class="panel spine">
    <span class="spine-text">Un nouveau matin !</span>
    <span class="spine-author">Kit<br>Marsh</span>
  </section>

  <section class="panel front">
    <svg class="cells" style="left:0;top:0" width="500" height="720" viewBox="0 0 500 720" role="img" aria-label="Motif de cellules vertes translucides à noyaux jaunes">
      <defs>
        <linearGradient id="front-cells" x1="0" y1="0" x2="1" y2="1">
          <stop offset="0" stop-color="#c6e08f"/>
          <stop offset="0.5" stop-color="#b9d97a"/>
          <stop offset="1" stop-color="#d3e06a"/>
        </linearGradient>
      </defs>
      <path d="M0 250 C40 220 90 230 100 290 C110 360 140 380 200 380 C260 380 300 430 360 440 C430 450 480 480 500 520 V720 H0 Z" fill="url(#front-cells)" opacity="0.85"/>
    </svg>
    <h1 class="title">
      <span class="small">Un</span>
      <span class="big">nouveau</span>
      <span class="big indent">matin !</span>
    </h1>
    <p class="subtitle">Condamné par la médecine<br>il guérit grâce au jeûne,<br>la détoxination,<br>et l’amour.</p>
    <p class="author">Kit<br>Marsh</p>
  </section>
</main>
</body>
</html>
```